Before And After Photo Folder

I need a folder for Verolo Cosmetic Clinic to show before and after pictures to clients. Many photos are on my website.
It has to be divided into the following categories:
Quelix
Dermal filler
Lip filler
Non surgical facelift
IPL
Vitrasol
Ostravique
Plasma Facial
Skinbooster

Thank you. Ilske

```html
<!DOCTYPE html>
<html lang="en">
<head>
<meta charset="utf-8">
<title>Verolo Cosmetic Clinic – Before and After Folder</title>
<link rel="stylesheet" href="https://fonts.googleapis.com/css2?family=Montserrat:wght@500;600;700&display=swap">
<style>
  :root {
    --backdrop: #979493;
    --paper: #ffffff;
    --paper-shade: #d9d9d9;
    --brand-blue: #0aa9ea;
    --label-blue: #0d5aa6;
    --tag-grey: #9a9a9a;
    --logo-grey: #8a8a8a;
    --phone-blue: #1aa3e3;
    --skin-light: #e7c4b0;
    --skin-mid: #c99078;
    --skin-deep: #a8654f;
    --skin-red: #d8684f;
  }
  * { box-sizing: border-box; margin: 0; padding: 0; }
  html, body { width: 1104px; height: 1200px; overflow: hidden; }
  body {
    background: var(--backdrop);
    font-family: "Montserrat", sans-serif;
    position: relative;
  }

  /* ---------- Outer spread ---------- */
  .outer-spread {
    position: absolute;
    left: 104px; top: 95px;
    width: 732px; height: 463px;
    background: var(--paper);
    overflow: hidden;
  }
  .back-cover {
    position: absolute; left: 0; top: 0;
    width: 366px; height: 463px;
    background: linear-gradient(180deg, #f4f4f4, #ececec 80%, #ffffff);
  }
  .front-photo {
    position: absolute; left: 366px; top: 0;
    width: 366px; height: 463px;
    background:
      radial-gradient(ellipse 120px 90px at 190px 300px, #e9dcd4 0%, rgba(233,220,212,0) 100%),
      radial-gradient(ellipse 90px 120px at 250px 120px, #e8d3c6 0%, rgba(232,211,198,0) 100%),
      linear-gradient(135deg, #d2d2d2 0%, #c6c4c3 45%, #dedcda 100%);
  }
  .spread-curves {
    position: absolute; left: 0; top: 0;
    width: 732px; height: 463px;
  }

  .results-grid {
    position: absolute;
    left: 11px; top: 7px;
    display: grid;
    grid-template-columns: repeat(3, 111px);
    column-gap: 2px;
    row-gap: 2px;
  }
  .treatment { display: flex; flex-direction: column; gap: 2px; }
  .shot { display: flex; height: 54px; }
  .shot__tag {
    width: 14px;
    background: var(--tag-grey);
    color: #ffffff;
    font-size: 7.5px;
    font-weight: 500;
    letter-spacing: 0.3px;
    writing-mode: vertical-rl;
    transform: rotate(180deg);
    display: flex; align-items: center; justify-content: center;
  }
  .shot__photo { flex: 1; }
  .photo--light { background: linear-gradient(180deg, var(--skin-light), var(--skin-mid)); }
  .photo--mid { background: linear-gradient(160deg, #d8a994, var(--skin-mid) 60%, #b97c66); }
  .photo--dark { background: linear-gradient(90deg, #2a2a2a 0 20%, #c7a08d 20%, #dcb7a4 70%, #f0ece9 100%); }
  .photo--red { background: linear-gradient(180deg, var(--skin-red), #c0563f 60%, #2b1a16); }
  .photo--pink { background: linear-gradient(180deg, #e2a89c, #dd9b92); }
  .photo--olive { background: linear-gradient(180deg, #b9ab98, #9a8b77); }
  .treatment__label {
    height: 17px;
    background: var(--label-blue);
    color: #ffffff;
    font-size: 9.5px;
    font-weight: 600;
    text-align: center;
    display: flex; align-items: center; justify-content: center;
    line-height: 1;
  }
  .treatment__label--two-line { font-size: 8.5px; line-height: 9px; }

  .phone {
    position: absolute;
    left: 162px; top: 431px;
    display: flex; align-items: center; gap: 3px;
    color: var(--phone-blue);
    font-size: 21px;
    font-weight: 700;
  }
  .phone svg { width: 18px; height: 18px; }

  .clinic-name {
    position: absolute;
    left: 420px; top: 372px;
    display: flex; align-items: center; gap: 10px;
  }
  .clinic-name__mark {
    width: 48px; height: 48px;
    border-radius: 50%;
    background: var(--brand-blue);
  }
  .clinic-name__text {
    color: var(--logo-grey);
    font-weight: 500;
    line-height: 1;
    text-align: center;
  }
  .clinic-name__main { display: block; font-size: 40px; letter-spacing: 1px; }
  .clinic-name__sub { display: block; font-size: 11.5px; letter-spacing: 0.5px; margin-top: 4px; }

  /* ---------- Inner spread ---------- */
  .inner-spread {
    position: absolute;
    left: 277px; top: 637px;
    width: 732px; height: 461px;
    background: linear-gradient(90deg,
      #ffffff 0%, #f3f3f3 30%, var(--paper-shade) 49.6%,
      #cfcfcf 49.9%, var(--paper-shade) 50.3%, #f3f3f3 70%, #ffffff 100%);
  }
  .pockets { position: absolute; left: 0; top: 0; width: 732px; height: 461px; }
</style>
</head>
<body>

  <section class="outer-spread" aria-label="Folder outside: back and front cover">
    <div class="back-cover"></div>
    <div class="front-photo" role="img" aria-label="Photo of a therapist applying a facial mask with a brush to a relaxed client"></div>

    <svg class="spread-curves" viewBox="0 0 732 463" aria-hidden="true">
      <path d="M340 368 C420 320 500 300 560 302 C640 306 700 330 732 356 L732 463 L340 463 Z" fill="var(--brand-blue)"/>
      <path d="M345 374 C420 346 500 338 560 340 C640 344 700 372 732 402 L732 463 L345 463 Z" fill="#ffffff"/>
      <path d="M0 398 C20 440 90 450 160 438 C240 424 300 398 350 370 L350 378 C300 404 240 432 160 446 C90 456 18 446 0 412 Z" fill="var(--brand-blue)"/>
      <path d="M0 398 C20 430 60 440 110 438" fill="none" stroke="#cfcfcf" stroke-width="1.5"/>
    </svg>

    <div class="back-cover-content">
      <div class="results-grid">
        <article class="treatment">
          <div class="shot"><span class="shot__tag">BEFORE</span><div class="shot__photo photo--mid" role="img" aria-label="Before photo of forehead and eyes"></div></div>
          <div class="shot"><span class="shot__tag">AFTER</span><div class="shot__photo photo--mid" role="img" aria-label="After photo of forehead and eyes"></div></div>
          <div class="treatment__label">QUELIX</div>
        </article>
        <article class="treatment">
          <div class="shot"><span class="shot__tag">BEFORE</span><div class="shot__photo photo--dark" role="img" aria-label="Before photo of smile lines"></div></div>
          <div class="shot"><span class="shot__tag">AFTER</span><div class="shot__photo photo--dark" role="img" aria-label="After photo of smile lines"></div></div>
          <div class="treatment__label">DERMAL FILLER</div>
        </article>
        <article class="treatment">
          <div class="shot"><span class="shot__tag">BEFORE</span><div class="shot__photo photo--light" role="img" aria-label="Before photo of lips"></div></div>
          <div class="shot"><span class="shot__tag">AFTER</span><div class="shot__photo photo--light" role="img" aria-label="After photo of lips"></div></div>
          <div class="treatment__label">LIP FILLER</div>
        </article>

        <article class="treatment">
          <div class="shot"><span class="shot__tag">BEFORE</span><div class="shot__photo photo--light" role="img" aria-label="Before photo of lower face"></div></div>
          <div class="shot"><span class="shot__tag">AFTER</span><div class="shot__photo photo--light" role="img" aria-label="After photo of lower face"></div></div>
          <div class="treatment__label treatment__label--two-line">NON SURGICAL<br>FACELIFT</div>
        </article>
        <article class="treatment">
          <div class="shot"><span class="shot__tag">BEFORE</span><div class="shot__photo photo--light" role="img" aria-label="Before photo of skin around the mouth"></div></div>
          <div class="shot"><span class="shot__tag">AFTER</span><div class="shot__photo photo--light" role="img" aria-label="After photo of skin around the mouth"></div></div>
          <div class="treatment__label">IPL</div>
        </article>
        <article class="treatment">
          <div class="shot"><span class="shot__tag">BEFORE</span><div class="shot__photo photo--mid" role="img" aria-label="Before photo of pigmented skin"></div></div>
          <div class="shot"><span class="shot__tag">AFTER</span><div class="shot__photo photo--pink" role="img" aria-label="After photo of even skin"></div></div>
          <div class="treatment__label">VITRASOL</div>
        </article>

        <article class="treatment">
          <div class="shot"><span class="shot__tag">BEFORE</span><div class="shot__photo photo--red" role="img" aria-label="Before photo of pigmented cheeks"></div></div>
          <div class="shot"><span class="shot__tag">AFTER</span><div class="shot__photo photo--red" role="img" aria-label="After photo of treated cheeks"></div></div>
          <div class="treatment__label">OSTRAVIQUE</div>
        </article>
        <article class="treatment">
          <div class="shot"><span class="shot__tag">BEFORE</span><div class="shot__photo photo--pink" role="img" aria-label="Before photo of cheek skin"></div></div>
          <div class="shot"><span class="shot__tag">AFTER</span><div class="shot__photo photo--pink" role="img" aria-label="After photo of cheek skin"></div></div>
          <div class="treatment__label">PLASMA FACIAL</div>
        </article>
        <article class="treatment">
          <div class="shot"><span class="shot__tag">BEFORE</span><div class="shot__photo photo--olive" role="img" aria-label="Before photo of lips and chin"></div></div>
          <div class="shot"><span class="shot__tag">AFTER</span><div class="shot__photo photo--olive" role="img" aria-label="After photo of lips and chin"></div></div>
          <div class="treatment__label">SKINBOOSTER</div>
        </article>
      </div>

      <div class="phone">
        <svg viewBox="0 0 20 20" aria-hidden="true">
          <circle cx="10" cy="10" r="10" fill="var(--phone-blue)"/>
          <path d="M7 5 L8.6 5 L9.4 7.6 L8.3 8.6 C8.9 10 10 11.1 11.4 11.7 L12.4 10.6 L15 11.4 L15 13 C15 13.6 14.5 14 13.9 14 C9.6 13.7 6.3 10.4 6 6.1 C6 5.5 6.4 5 7 5 Z" fill="#ffffff"/>
        </svg>
        <span>0800-555-019</span>
      </div>
    </div>

    <div class="clinic-name">
      <span class="clinic-name__mark" aria-hidden="true"></span>
      <span class="clinic-name__text">
        <span class="clinic-name__main">VEROLO</span>
        <span class="clinic-name__sub">COSMETIC CLINIC</span>
      </span>
    </div>
  </section>

  <section class="inner-spread" aria-label="Folder inside with two pockets">
    <svg class="pockets" viewBox="0 0 732 461" aria-hidden="true">
      <path d="M0 273 L322 273 Q333 273 335 285 L363 461 L0 461 Z" fill="var(--brand-blue)"/>
      <path d="M732 273 L404 273 Q392 273 390 285 L367 461 L732 461 Z" fill="var(--brand-blue)"/>
    </svg>
  </section>

</body>
</html>
```